Business Card

Just need business logo with phone number on it. 0487 312 556
And the following on the bottom of the card.

"Your local plumbing experts".
and emblems for kelpa card, cheque and cash

```html
<!DOCTYPE html>
<html lang="en">
<head>
<meta charset="utf-8">
<title>Ridgeline Plumbing &amp; Drainage – Business Card</title>
<link rel="stylesheet" href="https://fonts.googleapis.com/css2?family=Michroma&family=Roboto:wght@400;700&display=swap">
<style>
  :root {
    --backdrop: #2a2a2a;
    --paper: #f4f4f4;
    --brand-red: #d2261e;
    --brand-blue: #0a74c4;
    --band-mid: #6f5a78;
    --ink-light: #ffffff;
    --cheque-yellow: #f3e08a;
    --cheque-line: #8a7a3a;
    --cash-green: #5fa784;
  }
  html, body {
    margin: 0;
    width: 1200px;
    height: 902px;
    overflow: hidden;
    background: var(--backdrop);
  }
  .business-card {
    position: absolute;
    left: 100px;
    top: 145px;
    width: 1000px;
    height: 611px;
    border-radius: 40px;
    overflow: hidden;
    background: var(--paper);
  }
  .card-band {
    position: absolute;
    inset: 0;
  }
  .brand-name {
    position: absolute;
    right: 120px;
    top: 70px;
    margin: 0;
    text-align: right;
    color: var(--brand-red);
    font-family: "Michroma", sans-serif;
    font-weight: 400;
    line-height: 1.15;
  }
  .brand-name .brand-main {
    display: block;
    font-size: 58px;
    letter-spacing: 2px;
  }
  .brand-name .brand-sub {
    display: block;
    font-size: 21px;
    letter-spacing: 5px;
  }
  .brand-name .brand-legal {
    display: block;
    font-size: 11px;
    letter-spacing: 3px;
    margin-top: 4px;
  }
  .phone-row {
    position: absolute;
    left: 90px;
    top: 340px;
    display: flex;
    align-items: center;
    gap: 36px;
  }
  .phone-icon { width: 52px; height: 52px; }
  .phone-number {
    color: var(--ink-light);
    font-family: "Michroma", sans-serif;
    font-size: 60px;
    letter-spacing: 4px;
    white-space: nowrap;
  }
  .tagline-row {
    position: absolute;
    left: 90px;
    right: 90px;
    top: 440px;
    display: flex;
    align-items: center;
    gap: 24px;
  }
  .tagline-rule {
    flex: 1;
    height: 3px;
    background: var(--ink-light);
    opacity: 0.9;
  }
  .tagline {
    color: var(--ink-light);
    font-family: "Roboto", sans-serif;
    font-size: 30px;
    white-space: nowrap;
  }
  .payment-row {
    position: absolute;
    left: 90px;
    top: 520px;
    display: flex;
    align-items: center;
    gap: 22px;
    color: var(--ink-light);
    font-family: "Roboto", sans-serif;
    font-size: 24px;
  }
  .pay-card {
    width: 80px;
    height: 46px;
    border-radius: 5px;
    background: var(--ink-light);
    display: flex;
    align-items: center;
    justify-content: center;
    color: var(--brand-blue);
    font-weight: 700;
    font-size: 20px;
  }
  .pay-cheque, .pay-cash { width: 100px; height: 46px; }
</style>
</head>
<body>
  <main class="business-card">
    <svg class="card-band" viewBox="0 0 1000 611" preserveAspectRatio="none" aria-hidden="true">
      <defs>
        <linearGradient id="bandGradient" x1="0" y1="0" x2="0" y2="1">
          <stop offset="0.30" stop-color="#0a74c4"/>
          <stop offset="0.55" stop-color="#6f5a78"/>
          <stop offset="0.95" stop-color="#d2261e"/>
        </linearGradient>
      </defs>
      <path d="M0,150 C250,330 650,360 1000,300 L1000,611 L0,611 Z" fill="url(#bandGradient)"/>
    </svg>

    <h1 class="brand-name">
      <span class="brand-main">RIDGELINE</span>
      <span class="brand-sub">PLUMBING &amp; DRAINAGE</span>
      <span class="brand-legal">PTY LTD</span>
    </h1>

    <div class="phone-row">
      <svg class="phone-icon" viewBox="0 0 52 52" aria-hidden="true">
        <circle cx="26" cy="26" r="23" fill="none" stroke="#ffffff" stroke-width="3.5"/>
        <path d="M19 14 C16 16 15 20 17 25 C20 32 25 37 31 39 C35 40 38 38 39 35 L34 31 L31 33 C27 31 23 27 21 23 L23 20 Z" fill="#ffffff"/>
      </svg>
      <span class="phone-number">0487 312 556</span>
    </div>

    <div class="tagline-row">
      <span class="tagline-rule"></span>
      <span class="tagline">Your local plumbing experts</span>
      <span class="tagline-rule"></span>
    </div>

    <div class="payment-row">
      <span class="payment-label">Payment made from:</span>
      <span class="pay-card">kelpa</span>
      <svg class="pay-cheque" viewBox="0 0 100 46" role="img" aria-label="Cheque">
        <rect x="1" y="1" width="98" height="44" rx="3" fill="#f3e08a" stroke="#8a7a3a" stroke-width="1.5"/>
        <line x1="10" y1="22" x2="90" y2="22" stroke="#8a7a3a" stroke-width="2"/>
        <line x1="10" y1="32" x2="60" y2="32" stroke="#8a7a3a" stroke-width="2"/>
        <rect x="68" y="28" width="22" height="8" fill="none" stroke="#8a7a3a" stroke-width="1.5"/>
      </svg>
      <svg class="pay-cash" viewBox="0 0 100 46" role="img" aria-label="Cash">
        <rect x="1" y="1" width="98" height="44" rx="3" fill="#5fa784"/>
        <text x="50" y="30" text-anchor="middle" font-family="Roboto, sans-serif" font-size="18" fill="#ffffff">CA$H</text>
      </svg>
    </div>
  </main>
</body>
</html>
```